Murmelo advertising imagery for a 13.28kW solar system

Project Overview:
We are thrilled to announce a limited-time offer on our top-of-the-line 13.28kW Solar System! This Murmelo ad campaign aims to generate excitement and interest among homeowners and businesses looking to harness the power of solar energy. The special offer includes a competitively priced 13.28kW solar system starting from $5800, fully installed, and an exclusive free upgrade to the Vexalon 10kW 1 Phase inverter for a limited two-week period.

Target Audience:
Our target audience consists of environmentally conscious homeowners, small to medium-sized businesses, and those seeking to reduce their energy bills and carbon footprint. We will be focusing on customers in [your service area location] or nearby regions, aged between 25 to 65 years old.

Key Message:
The advertisement should convey the following key messages:

"Go Solar and Save Big on Your Energy Bills!"
"Upgrade to the Powerful Vexalon Inverter for Free - Limited Time Only!"
"High-Performance 13.28kW Solar System Fully Installed from $5800."
"Harness Clean and Renewable Energy to Power Your Home or Business."
Design Requirements:

Dimensions: The advertisement should comply with Murmelo's recommended ad dimensions (e.g., 1200 x 628 pixels).
Branding: Incorporate our company logo and colors (Logo attached).
Visuals: Use eye-catching images or animations that showcase solar panels, clean energy, and happy customers enjoying the benefits of solar power.
Call-to-Action (CTA): Include a prominent CTA button, such as "Get a Quote," "Limited Time Offer - Act Now!" or "Learn More."
Text: Keep the text clear, concise, and persuasive, highlighting the savings, eco-friendliness, and exclusive offer.
Pricing Details: Clearly mention the starting price of the 13.28kW solar system and emphasize the free upgrade to the Vexalon 10kW 1 Phase inverter.
Trust Signals: Incorporate any relevant awards, certifications, or customer testimonials to build trust and credibility.
Countdown Timer (Optional): Consider adding a countdown timer to create a sense of urgency and remind viewers about the limited-time offer.
Additional Information:

Include the following contact information: Website URL, phone number, and email address.
The advertisement should comply with Murmelo's advertising guidelines and policies.
Prominently display the duration of the offer: "Two Weeks Only - Act Fast!"

Target Market(s)

Industry/Entity Type

Solar Energy

Colors
0054AA
0677BA
7BADD7
CADEEF
E8F1F8

Requirements
Must have
• Key Message: The advertisement should convey the following key messages: "Go Solar and Save Big on Your Energy Bills!" "Upgrade to the Powerful Vexalon Inverter for Free - Limited Time Only!" "High-Performance 13.28kW Solar System Fully Installed from $5800." "Harness Clean and Renewable Energy to Power Your Home or Business."
Nice to have
• Must have picture of solar panels and the Vexalon 10kW 1 Phase inverter

```html
<!DOCTYPE html>
<html lang="en">
<head>
<meta charset="utf-8">
<title>Norvane Energy – 13.28kW Solar System Offer</title>
<link href="https://fonts.googleapis.com/css2?family=Montserrat:ital,wght@0,500;0,600;0,700;0,800;1,500;1,800&family=Raleway:wght@400;500&family=Playball&display=swap" rel="stylesheet">
<style>
  :root{
    --brand-red:#c9152b;
    --brand-red-dark:#a30f20;
    --navy:#1d2740;
    --ink:#222a36;
    --blue-deep:#0054aa;
    --blue-mid:#0677ba;
    --blue-soft:#7badd7;
    --blue-pale:#cadeef;
    --blue-mist:#e8f1f8;
    --gold:#e0a823;
    --white:#ffffff;
    --panel-grey:#f3f4f6;
    --icon-blue:#1a86e0;
  }
  *{box-sizing:border-box;margin:0;padding:0}
  html,body{width:1200px;height:677px;overflow:hidden;background:#ffffff}
  .ad{position:relative;width:1200px;height:677px;overflow:hidden;
      background:linear-gradient(180deg,#ffffff 0%,#fbfbfc 70%,var(--panel-grey) 100%);
      font-family:'Montserrat',sans-serif;color:var(--ink)}

  .brand-art{position:absolute;inset:0;width:1200px;height:677px}

  .logo{position:absolute;left:20px;top:28px;display:flex;align-items:center;gap:8px;
        font-weight:700;font-size:17px;color:var(--navy);letter-spacing:.5px;text-transform:uppercase}
  .logo-mark{width:16px;height:16px;background:var(--brand-red)}

  .offer-script{position:absolute;left:20px;top:78px;font-family:'Playball',cursive;font-size:34px;color:var(--brand-red);line-height:1}
  .offer-title{position:absolute;left:20px;top:122px;font-weight:700;font-size:26.5px;color:var(--ink);letter-spacing:.3px;line-height:1}
  .offer-price{position:absolute;left:171px;top:155px;width:190px;height:30px;background:var(--navy);border-radius:9px;
               color:var(--white);font-weight:800;font-style:italic;font-size:28px;line-height:30px;text-align:center;letter-spacing:.5px}
  .offer-note{position:absolute;left:17px;top:198px;font-style:italic;font-weight:500;font-size:14px;color:var(--ink)}

  .cta{position:absolute;left:44px;top:266px;width:318px;height:102px}
  .cta-shadow{position:absolute;left:10px;top:28px;width:240px;height:84px;border-radius:0 0 40px 40px;background:var(--brand-red-dark)}
  .cta-pill{position:absolute;left:0;top:0;width:318px;height:94px;border-radius:48px;
            background:linear-gradient(180deg,#e0213a 0%,var(--brand-red) 60%,var(--brand-red-dark) 100%)}
  .cta-main{position:absolute;left:60px;top:10px;color:var(--white);font-weight:800;font-size:36px;letter-spacing:.5px;line-height:1}
  .cta-sub{position:absolute;left:66px;top:52px;color:var(--white);font-weight:500;font-size:17px;letter-spacing:1.5px;line-height:1}
  .cta-small{position:absolute;right:62px;top:74px;color:var(--white);font-weight:600;font-size:12.5px;letter-spacing:1.6px;line-height:1}
  .stopwatch{position:absolute;left:14px;top:236px;width:84px;height:92px}

  .benefits{position:absolute;left:20px;top:416px;list-style:none}
  .benefits li{display:flex;align-items:center;gap:10px;height:32.7px;font-family:'Raleway',sans-serif;font-size:15.5px;color:var(--ink)}
  .benefits svg{flex:0 0 24px}

  .info-heading{position:absolute;left:20px;top:574px;font-weight:600;font-size:22px;color:var(--ink)}
  .contact{position:absolute;top:616px;display:flex;align-items:center;gap:12px;font-weight:500;font-size:16.5px;color:var(--ink)}
  .contact-web{left:20px}
  .contact-mail{left:344px}
  .contact-icon{width:38px;height:38px;border-radius:50%;background:var(--icon-blue);display:flex;align-items:center;justify-content:center}

  .call{position:absolute;left:808px;top:604px;display:flex;align-items:center;gap:18px}
  .call-label{font-weight:700;font-size:20px;color:var(--ink);line-height:1.05}
  .call-number{font-weight:700;font-size:27px;color:var(--brand-red);line-height:1.1}

  .guarantee-badge{position:absolute;left:532px;top:126px;width:120px;height:120px;border-radius:50%;background:var(--gold)}

  .panels-photo{position:absolute;left:818px;top:70px;width:318px;height:418px;border-radius:6px;
                background:linear-gradient(160deg,#3f50b8 0%,#2b3aa0 55%,#1f2d86 100%)}
  .inverter-photo{position:absolute;left:682px;top:302px;width:80px;height:140px;border-radius:8px;
                  background:linear-gradient(90deg,#eef0f3 0%,#d3d8de 70%,#2a2f38 100%)}
</style>
</head>
<body>
<main class="ad">

  <svg class="brand-art" viewBox="0 0 1200 677" aria-hidden="true">
    <defs>
      <linearGradient id="bluePanel" x1="0" y1="0" x2="1" y2="1">
        <stop offset="0" stop-color="#0a63b9"/>
        <stop offset="1" stop-color="#0050a6"/>
      </linearGradient>
    </defs>
    <path d="M810 0 C 690 120, 672 400, 790 557 L1200 557 L1200 0 Z" fill="url(#bluePanel)"/>
    <path d="M798 0 C 676 122, 660 402, 778 567" fill="none" stroke="var(--white)" stroke-width="7"/>
    <path d="M786 0 C 662 124, 646 404, 766 574" fill="none" stroke="var(--blue-deep)" stroke-width="5"/>
    <circle cx="722" cy="372" r="100" fill="var(--white)"/>
    <circle cx="722" cy="372" r="91" fill="var(--blue-deep)"/>
  </svg>

  <div class="logo"><span class="logo-mark"></span>Norvane Energy</div>

  <p class="offer-script">Limited-Time Offer</p>
  <h1 class="offer-title">13.28KW SOLAR SYSTEM</h1>
  <p class="offer-price">FOR $5800</p>
  <p class="offer-note">Free Vexalon inverter upgrade for a limited time.</p>

  <div class="cta">
    <div class="cta-shadow"></div>
    <div class="cta-pill"></div>
    <span class="cta-main">ACT NOW</span>
    <span class="cta-sub">Limited Time Offer</span>
    <span class="cta-small">Two Weeks Only</span>
  </div>
  <svg class="stopwatch" viewBox="0 0 84 92" aria-hidden="true">
    <rect x="36" y="2" width="12" height="8" rx="2" fill="var(--brand-red)"/>
    <rect x="64" y="12" width="10" height="7" rx="2" transform="rotate(40 69 15)" fill="var(--brand-red)"/>
    <circle cx="42" cy="50" r="40" fill="var(--white)" stroke="var(--brand-red)" stroke-width="5"/>
    <circle cx="42" cy="50" r="31" fill="none" stroke="var(--navy)" stroke-width="3"/>
    <line x1="42" y1="50" x2="42" y2="28" stroke="var(--navy)" stroke-width="3" stroke-linecap="round"/>
    <line x1="42" y1="50" x2="56" y2="60" stroke="var(--brand-red)" stroke-width="3" stroke-linecap="round"/>
    <circle cx="42" cy="50" r="3.5" fill="var(--navy)"/>
  </svg>

  <div class="guarantee-badge" aria-hidden="true"></div>

  <div class="panels-photo" role="img" aria-label="Photo of two blue monocrystalline solar panels standing side by side"></div>
  <div class="inverter-photo" role="img" aria-label="Photo of the Vexalon 10kW single-phase solar inverter"></div>

  <ul class="benefits">
    <li><svg width="24" height="22" viewBox="0 0 24 22" aria-hidden="true"><rect x="2" y="4" width="16" height="16" fill="none" stroke="var(--brand-red)" stroke-width="2.5"/><path d="M6 11 L10 16 L21 2" fill="none" stroke="var(--navy)" stroke-width="3"/></svg>Go Solar and Save Big on Your Energy Bills</li>
    <li><svg width="24" height="22" viewBox="0 0 24 22" aria-hidden="true"><rect x="2" y="4" width="16" height="16" fill="none" stroke="var(--brand-red)" stroke-width="2.5"/><path d="M6 11 L10 16 L21 2" fill="none" stroke="var(--navy)" stroke-width="3"/></svg>High-Performance 13.28kW Solar System Fully Installed from $5800</li>
    <li><svg width="24" height="22" viewBox="0 0 24 22" aria-hidden="true"><rect x="2" y="4" width="16" height="16" fill="none" stroke="var(--brand-red)" stroke-width="2.5"/><path d="M6 11 L10 16 L21 2" fill="none" stroke="var(--navy)" stroke-width="3"/></svg>Harness Clean and Renewable Energy to Power Your Home or Business.</li>
    <li><svg width="24" height="22" viewBox="0 0 24 22" aria-hidden="true"><rect x="2" y="4" width="16" height="16" fill="none" stroke="var(--brand-red)" stroke-width="2.5"/><path d="M6 11 L10 16 L21 2" fill="none" stroke="var(--navy)" stroke-width="3"/></svg>Upgrade to the Powerful Vexalon Inverter for Free - Limited Time Only</li>
  </ul>

  <h2 class="info-heading">For more info</h2>
  <div class="contact contact-web">
    <span class="contact-icon"><svg width="22" height="22" viewBox="0 0 24 24" aria-hidden="true" fill="none" stroke="#fff" stroke-width="1.8"><circle cx="12" cy="12" r="10"/><ellipse cx="12" cy="12" rx="4.5" ry="10"/><line x1="2" y1="12" x2="22" y2="12"/><path d="M4 6.5 H20 M4 17.5 H20"/></svg></span>
    www.norvaneenergy.com
  </div>
  <div class="contact contact-mail">
    <span class="contact-icon"><svg width="20" height="16" viewBox="0 0 20 16" aria-hidden="true"><rect x="1" y="1" width="18" height="14" rx="2" fill="#fff"/><path d="M2 3 L10 9 L18 3" fill="none" stroke="#1a86e0" stroke-width="1.8"/></svg></span>
    hello@norvaneenergy.com
  </div>

  <div class="call">
    <svg width="60" height="52" viewBox="0 0 60 52" aria-hidden="true">
      <path d="M4 18 C4 4, 56 4, 56 18 L56 22 L44 22 L44 15 C36 11, 24 11, 16 15 L16 22 L4 22 Z" fill="var(--brand-red)"/>
      <path d="M12 24 L48 24 L56 50 L4 50 Z" fill="var(--brand-red)"/>
      <g fill="#fff"><circle cx="22" cy="32" r="2.2"/><circle cx="30" cy="32" r="2.2"/><circle cx="38" cy="32" r="2.2"/><circle cx="22" cy="39" r="2.2"/><circle cx="30" cy="39" r="2.2"/><circle cx="38" cy="39" r="2.2"/><circle cx="22" cy="46" r="2.2"/><circle cx="30" cy="46" r="2.2"/><circle cx="38" cy="46" r="2.2"/></g>
    </svg>
    <div>
      <p class="call-label">Call Us</p>
      <p class="call-number">(014) 682 3150</p>
    </div>
  </div>

</main>
</body>
</html>
```